Real Estate Investing company needs a business card design

We need a business card design for new Real Estate Investment Company called "Maple Ridge Ventures, LLC." We buy homes for cash and close quickly in any situation. Our company provides an easy and fast option for home owners who are in tough situations who need to sell their home fast and don't want realtor fees or other listing hassles. We also renovate and resell our homes which helps provide housing for the community. We would like to see designs that use the colors blue and white to match our company logo or other colors that may match our company logo. The final design should communicate trust and easy process.
Industry/Entity Type
Business
Contact Information for Business Card
Front should have company name and company logo. back of card should have company logo and area to list services.
Look and feel

```html
<!DOCTYPE html>
<html lang="en">
<head>
<meta charset="utf-8">
<title>Maple Ridge Ventures – Business Card</title>
<link href="https://fonts.googleapis.com/css2?family=Source+Sans+3:wght@400;600;700;800&display=swap" rel="stylesheet">
<style>
  :root {
    --stage: #000000;
    --card-light: #f3f3f3;
    --brand-blue: #0a6fbf;
    --ink: #1c1c1c;
    --white: #ffffff;
  }
  * { margin: 0; padding: 0; box-sizing: border-box; }
  html, body {
    width: 1200px;
    height: 900px;
    overflow: hidden;
    background: var(--stage);
    font-family: "Source Sans 3", Arial, sans-serif;
  }
  .canvas { position: relative; width: 1200px; height: 900px; }

  .card { position: absolute; top: 200px; width: 310px; height: 502px; }

  .card-front {
    left: 265px;
    background: var(--card-light);
    border-radius: 52px 0 52px 0;
    color: var(--ink);
  }
  .card-back {
    left: 641px;
    width: 309px;
    background: var(--brand-blue);
    border-radius: 0 52px 0 52px;
    color: var(--white);
  }

  .wordmark {
    position: absolute;
    left: 0; right: 0;
    text-align: center;
    font-weight: 800;
    line-height: 1;
    letter-spacing: 0.5px;
  }
  .card-front .wordmark { top: 54px; color: var(--brand-blue); font-size: 34px; }
  .card-back .wordmark { top: 58px; color: var(--white); font-size: 34px; }
  .wordmark span { display: block; }
  .wordmark .line-sub { font-size: 28px; margin-top: 4px; }

  .contact { position: absolute; left: 29px; top: 338px; }
  .contact-name { color: var(--brand-blue); font-size: 19px; font-weight: 600; line-height: 1.1; }
  .contact-role { font-size: 14px; margin-top: 3px; }
  .contact-list { list-style: none; margin-top: 14px; font-size: 14px; }
  .contact-list li { display: flex; align-items: center; height: 21px; }
  .contact-list svg { width: 10px; height: 10px; margin-right: 7px; fill: var(--brand-blue); }
  .contact-address { margin-top: 12px; font-size: 14px; line-height: 16px; margin-left: -2px; }

  .services { position: absolute; left: 17px; top: 209px; width: 270px; list-style: none; }
  .services li {
    position: relative;
    padding-left: 17px;
    font-size: 14px;
    font-weight: 600;
    line-height: 18px;
    margin-bottom: 21px;
  }
  .services li::before {
    content: "";
    position: absolute;
    left: 0; top: 6px;
    width: 8px; height: 8px;
    border-radius: 50%;
    background: var(--white);
  }
</style>
</head>
<body>
<main class="canvas">
  <section class="card card-front">
    <div class="wordmark">
      <span class="line-main">MAPLE RIDGE</span>
      <span class="line-sub">VENTURES</span>
    </div>
    <div class="contact">
      <p class="contact-name">Daniel Hayes</p>
      <p class="contact-role">Managing Director</p>
      <ul class="contact-list">
        <li>
          <svg viewBox="0 0 24 24" aria-hidden="true"><path d="M6.6 10.8a15.1 15.1 0 0 0 6.6 6.6l2.2-2.2c.3-.3.7-.4 1-.2 1.1.4 2.3.6 3.6.6.6 0 1 .4 1 1V20c0 .6-.4 1-1 1A17 17 0 0 1 3 4c0-.6.4-1 1-1h3.5c.6 0 1 .4 1 1 0 1.3.2 2.5.6 3.6.1.3 0 .7-.2 1z"/></svg>
          (044)-555-0142
        </li>
        <li>
          <svg viewBox="0 0 24 24" aria-hidden="true"><path d="M2 5h20v14H2z M2 5l10 8 10-8" fill="var(--brand-blue)"/><path d="M3 6l9 7 9-7" fill="none" stroke="#f3f3f3" stroke-width="2"/></svg>
          info@mapleridgeventures.com
        </li>
      </ul>
      <p class="contact-address">12345, Address Goes Here<br>Country Name, 123456</p>
    </div>
  </section>

  <section class="card card-back">
    <div class="wordmark">
      <span class="line-main">MAPLE RIDGE</span>
      <span class="line-sub">VENTURES</span>
    </div>
    <ul class="services">
      <li>We buy homes for cash and close quickly in any situation.</li>
      <li>Our company provides an easy and fast option for home owners who are in tough situations who need to sell their home fast and don't want realtor fees or other listing hassles.</li>
      <li>We also renovate and resell our homes which helps provide housing for the community.</li>
    </ul>
  </section>
</main>
</body>
</html>
```